Layout für unsere Stellenanzeigen
Zielgruppe
Wir sind spezialisiert auf die Personalvermittlung von Medizinischen Fachkräften! Krankenschwestern - Altenpfleger u.s.w....!
Aufgabenstellung
Es soll nicht überladen sein - gerne kreativ witzig. Bitte einmal über unsere Homepage schauen. Wir arbeiten mit den Farben grün grau und schwarz. Pantonen anbei! Wir haben unsere Stil komplett auf Strichmännchen - Cartoon ausgelegt. Vielleicht gibt es hier Ideen diese Strichmännchen mit Realen Bilder zu kombinieren!!??!
Anlage:

```html
<!DOCTYPE html>
<html lang="de">
<head>
<meta charset="utf-8">
<title>Stellenanzeige Pflegewerk</title>
<link href="https://fonts.googleapis.com/css2?family=Ubuntu:ital,wght@0,400;0,500;0,700;1,700&display=swap" rel="stylesheet">
<style>
  :root {
    --green: #1f9a48;
    --grey: #6f6f72;
    --paper: #ffffff;
    --backdrop: #f2f1ec;
    --photo-warm: #e8dccb;
    --photo-cool: #cfe3e2;
  }
  * { box-sizing: border-box; margin: 0; padding: 0; }
  html, body { width: 1200px; height: 817px; overflow: hidden; background: var(--backdrop); }
  body { font-family: "Ubuntu", sans-serif; position: relative; }

  .flyer {
    position: absolute; left: 325px; top: 20px;
    width: 550px; height: 778px;
    background: var(--paper); overflow: hidden;
    box-shadow: 0 2px 10px rgba(0,0,0,.12);
  }

  .photo {
    position: absolute; left: 0; top: 100px; width: 550px; height: 280px;
    background: linear-gradient(100deg, var(--photo-warm) 0%, #efe7dc 45%, var(--photo-cool) 100%);
  }
  .header-shape { position: absolute; left: 0; top: 0; width: 550px; height: 240px; }

  .brand {
    position: absolute; left: 26px; top: 22px;
    display: flex; align-items: center; gap: 10px;
  }
  .brand-dot { width: 40px; height: 40px; border-radius: 50%; background: var(--green); }
  .brand-name { font-weight: 700; font-size: 24px; color: var(--green); }

  .headline {
    position: absolute; left: 220px; top: 22px; width: 310px;
    color: var(--green);
  }
  .headline-lead { font-size: 14px; font-weight: 500; margin-left: 8px; line-height: 1.2; }
  .headline-job { font-size: 20px; font-weight: 700; line-height: 1.12; }

  .slogan {
    position: absolute; left: 0; top: 282px; width: 380px; height: 92px;
    background: var(--green); border-radius: 0 0 18px 0;
    display: flex; align-items: center; padding-left: 28px;
  }
  .slogan-text {
    color: #fff; font-weight: 700; font-style: italic; font-size: 31px;
    line-height: 1.08; text-transform: uppercase; letter-spacing: .5px;
  }

  .bubble {
    position: absolute; left: 400px; top: 318px; width: 104px; height: 80px;
    background: var(--green); border-radius: 50%;
    color: #fff; font-size: 12px; font-weight: 500; line-height: 1.15;
    display: flex; align-items: center; justify-content: center; text-align: center;
  }
  .bubble::after {
    content: ""; position: absolute; left: 28px; bottom: -12px;
    border-left: 10px solid transparent; border-right: 10px solid transparent;
    border-top: 16px solid var(--green);
  }

  .intro {
    position: absolute; left: 24px; top: 392px; width: 360px;
    color: var(--green); font-size: 12px; line-height: 1.4;
  }
  .intro p + p { margin-top: 7px; }

  .contact-band {
    position: absolute; left: 0; top: 562px; width: 550px; height: 216px;
    background: var(--grey);
  }
  .contact-brand {
    position: absolute; left: 26px; top: 22px;
    display: flex; align-items: center; gap: 10px;
  }
  .contact-brand .brand-dot { background: #fff; width: 44px; height: 44px; }
  .contact-brand .brand-name { color: #fff; font-size: 22px; }
  .address {
    position: absolute; left: 26px; top: 84px;
    color: #e4e4e6; font-size: 11.5px; line-height: 1.45;
  }
  .phones {
    position: absolute; left: 190px; top: 84px;
    color: #fff; font-size: 11.5px; line-height: 1.45;
  }

  .character {
    position: absolute; left: 395px; top: 420px; width: 130px; height: 300px;
    background: linear-gradient(180deg, #f7f7f7 0%, #e9f2ec 55%, #f3f3f3 100%);
    border-radius: 60px 60px 20px 20px;
  }
  .tag {
    position: absolute; left: 280px; top: 592px; width: 110px; height: 22px;
    background: #8a8a8d; color: #fff; font-size: 13px;
    border-radius: 11px 3px 3px 11px;
    display: flex; align-items: center; justify-content: center;
  }

  .web {
    position: absolute; right: 0; bottom: 0; width: 210px; height: 40px;
    background: var(--paper); border-radius: 14px 0 0 0;
    color: var(--green); font-weight: 700; font-size: 17px;
    display: flex; align-items: center; justify-content: center;
  }
</style>
</head>
<body>
  <article class="flyer">
    <div class="photo" role="img" aria-label="Foto: Pflegerin hält die Hand einer älteren Person im Rollstuhl"></div>

    <svg class="header-shape" viewBox="0 0 550 240" aria-hidden="true">
      <path d="M0 0 H550 V182 C430 186 300 200 200 222 C120 240 60 238 0 234 Z" fill="#ffffff"/>
      <path d="M0 146 C140 148 260 156 360 166 C430 172 490 170 550 164 L550 172 C490 178 430 180 360 174 C260 164 140 156 0 154 Z" fill="var(--green)"/>
    </svg>

    <div class="brand">
      <span class="brand-dot"></span>
      <span class="brand-name">Pflegewerk</span>
    </div>

    <div class="headline">
      <div class="headline-lead">Wir suchen</div>
      <div class="headline-job">GESUNDHEITS- UND<br>KRANKENPFLEGER/IN<br>oder KINDERKRANKEN-<br>PFLEGER/IN!</div>
    </div>

    <div class="slogan">
      <div class="slogan-text">Zeig uns wo<br>der Kittel hängt!</div>
    </div>

    <div class="bubble">Wir freuen<br>uns auf<br>Ihre<br>Anfrage!</div>

    <div class="intro">
      <p>Sie sind verantwortungsbewusst, können selbstständig arbeiten, sind erfahren in der Pflege und im Umgang mit chronisch Kranken?</p>
      <p>Sie arbeiten gerne eigenverantwortlich von zu Hause aus, sind trotzdem reisefreudig (Ba-Wü), schätzen einen Dienstwagen der Mittelklasse - auch zur privaten Nutzung und suchen eine überwiegend organisatorische und beratende Tätigkeit, die spannend und gut bezahlt ist?</p>
    </div>

    <div class="contact-band">
      <div class="contact-brand">
        <span class="brand-dot"></span>
        <span class="brand-name">Pflegewerk</span>
      </div>
      <div class="address">
        Pflegewerk<br>
        Personalservice GmbH<br>
        Jonas Berthold<br>
        Lindenhof 12<br>
        77654 Musterstadt
      </div>
      <div class="phones">
        Tel.: 07821 - 390 412 0<br>
        Fax: 07821 - 390 412 9<br>
        Mobil: 0171 55 48 306<br>
        jonas.berthold@pflegewerk.de
      </div>
    </div>

    <div class="character" role="img" aria-label="Illustration: gezeichnete Pflegerin als Strichfigur in grünem Kasack"></div>
    <div class="tag">Home Office</div>

    <div class="web">www.pflegewerk.de</div>
  </article>
</body>
</html>
```